Business Card Design for a Personal Trainer

I need a business card design for my job as a personal trainer. It should have a unique, modern and exclusive design. On the front there should be only my logo with my name and my job. 0163/2918374 Tobias Kellinger Lindenfeldweg 14 80412 Munich Germany The most important contact information is the web adress. it can be bigger than the rest, but its not necessary. The card should be 8,5cmx5,5cm big. Font: Roboto. Colors: black, white, gray, 56c1ff.

```html
<!DOCTYPE html>
<html lang="de">
<head>
<meta charset="utf-8">
<title>Tobias Kellinger – Personal Trainer Visitenkarte</title>
<link href="https://fonts.googleapis.com/css2?family=Roboto:wght@300;400;500&display=swap" rel="stylesheet">
<style>
  :root {
    --stage: #7a7a7a;
    --card-dark: #4d4d4d;
    --card-light: #e9e9e9;
    --ink-dark: #161616;
    --ink-light: #ffffff;
    --photo-hi: #8c8c8c;
    --photo-lo: #2e2e2e;
  }
  * { margin: 0; padding: 0; box-sizing: border-box; }
  html, body { width: 1200px; height: 900px; overflow: hidden; }
  body {
    background: var(--stage);
    font-family: "Roboto", Arial, sans-serif;
    position: relative;
  }
  .card {
    position: absolute;
    overflow: hidden;
  }
  .card--back {
    left: 120px; top: 275px; width: 478px; height: 295px;
    background: var(--card-dark);
    border-radius: 0 48px 0 48px;
    color: var(--ink-light);
  }
  .portrait {
    position: absolute;
    left: 0; top: 0; width: 262px; height: 295px;
    background: radial-gradient(ellipse 55% 70% at 45% 55%, var(--photo-hi), var(--card-dark) 75%),
                linear-gradient(180deg, var(--card-dark), var(--photo-lo));
    background-blend-mode: normal;
  }
  .identity {
    position: absolute;
    left: 207px; top: 97px; width: 240px;
    text-align: center;
  }
  .identity__name {
    font-weight: 400;
    font-size: 24.5px;
    letter-spacing: 0.2px;
    white-space: nowrap;
    line-height: 1;
  }
  .identity__role {
    display: flex; align-items: center; gap: 6px;
    margin-top: 4px;
    font-size: 11px;
    letter-spacing: 2.6px;
    white-space: nowrap;
  }
  .identity__role::before, .identity__role::after {
    content: ""; flex: 1; height: 1px; background: currentColor;
  }
  .contact {
    position: absolute;
    left: 247px; top: 163px;
    list-style: none;
    font-size: 15.5px;
    line-height: 20px;
  }
  .contact li { display: flex; align-items: center; gap: 5px; }
  .contact svg { width: 14px; height: 14px; fill: var(--ink-light); }
  .address {
    position: absolute;
    left: 248px; top: 232px;
    font-style: normal;
    font-size: 15.5px;
    line-height: 19.5px;
  }
  .card--front {
    left: 620px; top: 276px; width: 476px; height: 293px;
    background: var(--card-light);
    border-radius: 48px 0 48px 0;
    color: var(--ink-dark);
    text-align: center;
  }
  .brand {
    position: absolute;
    left: 0; right: 0; top: 95px;
    display: flex; justify-content: center; align-items: center; gap: 10px;
    font-weight: 500;
    font-size: 22px;
    letter-spacing: 1px;
    text-transform: uppercase;
  }
  .brand__square { width: 16px; height: 16px; background: var(--ink-dark); }
  .card--front .identity {
    left: 86px; top: 176px; width: 302px;
  }
  .card--front .identity__name { font-size: 31px; }
  .card--front .identity__role { font-size: 13px; letter-spacing: 3px; margin-top: 3px; }
</style>
</head>
<body>
  <section class="card card--back">
    <div class="portrait" role="img" aria-label="Schwarz-Weiß-Porträt des Personal Trainers im Sportshirt"></div>
    <div class="identity">
      <h2 class="identity__name">TOBIAS KELLINGER</h2>
      <p class="identity__role">PERSONAL TRAINER</p>
    </div>
    <ul class="contact">
      <li><svg viewBox="0 0 16 16" aria-hidden="true"><path d="M2 5c0-2 2-3 6-3s6 1 6 3v1h-3V5H5v1H2zM4 7h8l2 6H2z"/></svg>0163/2918374</li>
      <li><svg viewBox="0 0 16 16" aria-hidden="true"><path d="M1 3h14v10H1zM2 4.5v.5l6 4 6-4v-.5z" fill-rule="evenodd"/></svg>t.kellinger@mxl.de</li>
      <li><svg viewBox="0 0 16 16" aria-hidden="true"><circle cx="8" cy="8" r="6.5"/></svg>www.tobiaskellinger.de</li>
    </ul>
    <address class="address">Lindenfeldweg 14<br>80412 München</address>
  </section>

  <section class="card card--front">
    <div class="brand"><span class="brand__square"></span>Kellinger Training</div>
    <div class="identity">
      <h1 class="identity__name">TOBIAS KELLINGER</h1>
      <p class="identity__role">PERSONAL TRAINER</p>
    </div>
  </section>
</body>
</html>
```